Zielgruppe
Verkauf und Einbau von Fenstern, Haustüren, Rollläden, Raffstore, Markisen, Insektenschutzgitter, Plissees
Aufgabenstellung
Es soll das gleiche Farbschema meines Firmenlogos haben. Grauer Hintergrund, kleine gelbe Akzente und schwarze Schrift

```html
<!DOCTYPE html>
<html lang="de">
<head>
<meta charset="utf-8">
<title>Rahmenwerk – Fenster, Haustüren, Sonnenschutz</title>
<link rel="stylesheet" href="https://fonts.googleapis.com/css2?family=Figtree:wght@400;500&family=Montserrat:wght@400;500;600&display=swap">
<style>
  :root {
    --canvas: #e2e2e2;
    --nav-grey: #c9c9c9;
    --hero-grey-light: #d6d6d6;
    --hero-grey-mid: #b9b9b9;
    --hero-grey-dark: #a4a4a4;
    --accent-yellow: #e0ac0f;
    --button-gold: #e7b416;
    --text-dark: #141414;
  }
  * { margin: 0; padding: 0; box-sizing: border-box; }
  html, body {
    width: 1200px; height: 1200px; overflow: hidden;
    background: var(--canvas);
  }
  .website {
    position: absolute; left: 0; top: 262px;
    width: 1200px; height: 677px; overflow: hidden;
    font-family: "Montserrat", sans-serif; color: var(--text-dark);
  }
  .hero-photo {
    position: absolute; inset: 0;
    background:
      radial-gradient(ellipse at 28% 40%, rgba(235,235,235,0.8), transparent 45%),
      radial-gradient(ellipse at 80% 70%, rgba(170,170,170,0.6), transparent 50%),
      linear-gradient(135deg, var(--hero-grey-light) 0%, var(--hero-grey-mid) 55%, var(--hero-grey-dark) 100%);
  }
  .main-nav {
    position: absolute; left: 0; top: 0; width: 100%; height: 75px;
    background: var(--nav-grey);
    font-family: "Figtree", sans-serif; font-size: 17px; font-weight: 500;
  }
  .main-nav a {
    position: absolute; top: 27px; color: var(--text-dark); text-decoration: none;
  }
  .main-nav a.is-active::after {
    content: ""; position: absolute; left: 0; bottom: -4px; width: 36px; height: 1.5px;
    background: var(--text-dark);
  }
  .brand-mark {
    position: absolute; left: 547px; top: 150px; width: 106px; height: 106px;
    border: 5px solid var(--accent-yellow); border-radius: 50%;
  }
  .brand-name {
    position: absolute; left: 0; top: 322px; width: 100%; text-align: center;
    font-size: 40px; font-weight: 500; letter-spacing: 1px; line-height: 44px;
    color: var(--accent-yellow); text-transform: uppercase;
  }
  .brand-tagline {
    position: absolute; left: 0; top: 370px; width: 100%; text-align: center;
    font-size: 15.5px; font-weight: 500; letter-spacing: 0.3px; text-transform: uppercase;
  }
  .welcome-title {
    position: absolute; left: 0; top: 424px; width: 100%; text-align: center;
    font-size: 15px; font-weight: 600; letter-spacing: 3.5px;
  }
  .welcome-text {
    position: absolute; left: 0; top: 466px; width: 100%; text-align: center;
    font-size: 13.5px; font-weight: 500; letter-spacing: 1px; line-height: 19px;
  }
  .contact-button {
    position: absolute; left: 523px; top: 540px; width: 152px; height: 41px;
    background: var(--button-gold); color: var(--text-dark);
    font-family: "Figtree", sans-serif; font-size: 14px; font-weight: 500;
    display: flex; align-items: center; justify-content: center;
    text-decoration: none; box-shadow: 0 2px 4px rgba(0,0,0,0.25);
  }
  .social-link {
    position: absolute; left: 59px; top: 594px;
    display: flex; align-items: center; gap: 8px;
    font-family: "Figtree", sans-serif; font-size: 14px; color: var(--text-dark);
    text-decoration: none;
  }
  .social-link .circle {
    width: 33px; height: 33px; border: 1.5px solid var(--text-dark); border-radius: 50%;
  }
  .footer-links a {
    position: absolute; top: 634px; color: var(--text-dark); text-decoration: none;
    font-family: "Figtree", sans-serif; font-size: 14.5px; font-weight: 500;
  }
</style>
</head>
<body>
  <main class="website">
    <div class="hero-photo" role="img" aria-label="Foto: Hände eines Tischlers beim Sägen von Holz, umgeben von Hobelspänen und Werkzeug"></div>

    <nav class="main-nav">
      <a class="is-active" href="#" style="left:63px">Startseite</a>
      <a href="#" style="left:197px">Produkte</a>
      <a href="#" style="left:348px">Abgeschlossene Projekte</a>
      <a href="#" style="left:600px">Wer wir sind</a>
      <a href="#" style="left:1051px">Kontakt</a>
    </nav>

    <div class="brand-mark"></div>
    <h1 class="brand-name">Rahmenwerk</h1>
    <p class="brand-tagline">Fenster Haustüren Sonnenschutz</p>

    <h2 class="welcome-title">WILLKOMMEN</h2>
    <p class="welcome-text">Verkauf und Einbau von Fenstern, Haustüren, Rollläden,<br>Raffstore, Markisen, Insektenschutzgitter, Plissees</p>

    <a class="contact-button" href="#">Kontaktieren</a>

    <a class="social-link" href="#"><span class="circle"></span>Folgen</a>

    <div class="footer-links">
      <a href="#" style="left:936px">Impressum</a>
      <a href="#" style="left:1067px">Datenschutz</a>
    </div>
  </main>
</body>
</html>
```